Quorvantix (real estate analytics tool) - LinkedIn and Facebook Cover Page

We are a newly launched SaaS startup which specialises in market analytics for commercial, office and retail property sector: https://quorvantix.com.au/
We need two images designed to serve as cover pages for LinkedIn and Facebook business pages. The images should be same/similar, however adjusted to fit the cover image specifications of each platform (LinkedIn: 1128 (w) x 191 (h) pixels https://www.velmorix.com/help/velmorix/answer/b718204/image-specifications-for-your-velmorix-pages-and-career-pages AND Facebook 1:8 aspect ration https://www.zantrelo.com/help/937462018573914)
The design should communicate analytics / analysis / people working on computers / perhaps with some playful aspects. The design should utilise our primary green colour (#1c7d39).
The attached screenshot shows the first attempt which we DO NOT like. It has no flow, it feels broken, the way the profile picture overlays the cover image is not great and feels broken.
Real Estate
- Caviar Dreams, Comfortaa

```html
<!DOCTYPE html>
<html lang="en">
<head>
<meta charset="utf-8">
<title>Quorvantix – Cover Banner</title>
<link rel="stylesheet" href="https://fonts.googleapis.com/css2?family=Comfortaa:wght@400;600;700&display=swap">
<style>
  :root {
    --bg: #ffffff;
    --ink: #1f1f1f;
    --ink-soft: #2b2b2b;
    --accent: #5ce21c;
    --accent-deep: #1c7d39;
    --accent-light: #8ff05a;
    --photo-dark: #3b3631;
    --photo-mid: #8a7a68;
    --photo-light: #d9cfc2;
    --glow: #7fe9f0;
  }
  * { margin: 0; padding: 0; box-sizing: border-box; }
  html, body { width: 1200px; height: 203px; overflow: hidden; background: var(--bg); }
  .cover {
    position: relative;
    width: 1200px;
    height: 203px;
    background: var(--bg);
    font-family: "Comfortaa", "Trebuchet MS", sans-serif;
    color: var(--ink);
    overflow: hidden;
  }
  .cover__shapes { position: absolute; inset: 0; }
  .brand {
    position: absolute;
    left: 94px;
    top: 20px;
    display: flex;
    align-items: center;
    gap: 10px;
  }
  .brand__dot {
    width: 30px;
    height: 30px;
    border-radius: 50%;
    background: var(--accent-deep);
  }
  .brand__name {
    font-size: 26px;
    font-weight: 700;
    color: var(--ink);
    letter-spacing: 0.2px;
  }
  .headline {
    position: absolute;
    left: 93px;
    top: 74px;
    font-size: 32px;
    font-weight: 600;
    line-height: 39px;
    color: var(--ink);
    letter-spacing: 0.3px;
  }
  .headline__accent { color: var(--accent); }
  .tagline {
    position: absolute;
    left: 94px;
    top: 163px;
    font-size: 15.5px;
    font-weight: 600;
    color: var(--ink-soft);
  }
</style>
</head>
<body>
  <div class="cover">
    <svg class="cover__shapes" width="1200" height="203" viewBox="0 0 1200 203" xmlns="http://www.w3.org/2000/svg">
      <defs>
        <linearGradient id="photoTone" x1="0" y1="0" x2="1" y2="1">
          <stop offset="0" stop-color="var(--photo-light)"/>
          <stop offset="0.45" stop-color="var(--photo-mid)"/>
          <stop offset="1" stop-color="var(--photo-dark)"/>
        </linearGradient>
        <radialGradient id="screenGlow" cx="0.55" cy="0.35" r="0.45">
          <stop offset="0" stop-color="var(--glow)" stop-opacity="0.55"/>
          <stop offset="1" stop-color="var(--glow)" stop-opacity="0"/>
        </radialGradient>
      </defs>

      <!-- bottom-left accent wedge -->
      <polygon class="wedge-left" points="0,88 0,203 38,203" fill="var(--accent)"/>

      <!-- photo area -->
      <g role="img" aria-label="Person working on a laptop with floating SaaS and analytics icons">
        <polygon points="722,0 1200,0 1200,203 778,203" fill="url(#photoTone)"/>
        <polygon points="722,0 1200,0 1200,203 778,203" fill="url(#screenGlow)"/>
      </g>

      <!-- green bands framing the photo -->
      <polygon class="band band--left" points="690,0 734,0 790,203 756,203" fill="var(--accent)"/>
      <polygon class="band band--left-light" points="734,0 748,0 800,203 790,203" fill="var(--accent-light)" opacity="0.8"/>
      <polygon class="band band--right" points="1140,62 1172,62 1200,150 1200,203 1186,203" fill="var(--accent)"/>
      <polygon class="band band--top" points="1150,0 1200,0 1200,30 1168,30" fill="var(--accent)" opacity="0.9"/>
    </svg>

    <div class="brand">
      <span class="brand__dot"></span>
      <span class="brand__name">Quorvantix</span>
    </div>

    <h1 class="headline">
      Analytics and <span class="headline__accent">Insights Tool</span> for the<br>
      <span class="headline__accent">Commercial</span> Property Market
    </h1>

    <p class="tagline">Quorvantix tracks over 100,000 commercial and retail properties</p>
  </div>
</body>
</html>
```